Implant and Mini Implant trifold brochure.

Logo is attached. Our website: www.q7zdental.com

We need an Implant and Mini Implant Flyer (on the same flyer) to be done by someone experienced in Dental marketing.

To be mailed via : Whole Route Bulk Post-Retail® (WRBP Retail®)
You need to put a Retail Indica
Reference: https://www.kelvanpost.net/business/whole-route-bulk-post.htm
Whole Route Bulk Post-Retail Indicia Guidelines

Every WRBP mailpiece must have an WRBP indicia with “ECRWSS” in the address area, within the permit indicia, or below the permit, like the examples to the right.
The WRBP Retail Indicia does not have a specific size requirement but must be larger than .5" x .5".
The type font must be in all caps and at least a 4 point size.
Place the indicia in the upper right hand corner of the mailpiece.
It should fit in the area 1.625" from the right edge and 1.375" from top edge.
Leave 1/8" of space around the top and right edge.

There should be a picture of a senior citizen eating apple - that is what implants will provide.

One side English; Other side Spanish.

If you do not have idea on what implants and mini-implants are then please ask specific questions.

Make space for specials.

Target Market(s)

dental implants, dental mini implants

Font styles to use
Other font styles liked:
• leaving it open for designer.

Colors
00a990
33b8a4
87cfc6
cadf82

Requirements
Must have
• A senior citizen eating apple - that is what implants allow people to do.
• Once the design layout is finalized, we will provide text. I am leaving the design wide open. you may look at good templates for ideas, but please respect the copyright.
Nice to have
• Use implant and mini implant pictures.
• Images needed
• 1) 3 Easy Steps to Implant Restoration in 1 visit: Use three images: mouth with missing teeth; mouth with implant screws fitted; mouth with teeth restored.
• 2) Image for Implant based Denture.
• 3) Senior Citizen or a couple eating apple.
• Image must be of good quality; even if taken from different sources they must gel well with the over all design. The final design has to be stunning.
• Please do not provide me with designs that I can get from any printing company.
• The Text area:
• 1. Why Implants?
• 2. Space for implant based dentures.
• 3. Other spaces for filling in "Why visit Q7z Dental"
• Additional Info: Time to use the following text in the final output.
• Q7z Dental - Your home for Quartz-7-Zenith Dental care.
• Q7z Dental - Your Implant Destination.
• Why Implants?
• . Durable, long lasting teeth replacement
• . Surgically implanted metal posts or frames into the jawbone
• . Allows crowns, bridges or complete dentures to be placed on implants
• Why Implant Dentures?
• . Durable and Cost Effective
• . Your denture fabricated as normal denture
• . Four or more implants are placed in one visit
• . Your denture is then retrofitted to snap on the mini implant retention head
• . Stabilize your loose dentures in one visit
• Why Mini Implants?
• . Less involved procedure than conventional implants
• . Usually completed in one dental appointment
• . Replace missing teeth instantly
• Implants vs Mini-Implants
• Visit Q7z Dental for a complementary consultation to learn which option is best for you. Depending on various conditions including that of the jawbone, you may be recommended an implant or mini-implant based treatment.
• Implant or Mini-implant treatment may not be suitable for all patients. For implants to be successful, you need to have healthy gums and adequate bones to support the implants. You must also be willing to commit to proper maintenance of your implants or dentures. Visit your dentist at Q7z Dental to learn more.
• Spanish translation from google added below:
• Q7z Dental: su casa para atención Quartz-7-Zenith dental.
• Q7z Dental: su destino de implante.
• ¿Por qué los implantes?
• . Reemplazo duradero y duradero de los dientes
• . Puestos o marcos de metal implantados quirúrgicamente en la mandíbula
• . Permiten para colocan coronas, puentes o dentaduras completas en implantes
• ¿Por qué las dentaduras postizas?
• . Durable y rentable
• . Su dentadura fabricada como dentadura normal
• . Cuatro o más implantes se colocan en una visita
• . Su dentadura se reajusta para encajar en el cabezal de retención mini implante
• . Estabilice sus dentaduras sueltas en una visita
• ¿Por qué Mini Implantes?
• . Procedimiento menos complicado que los implantes convencionales
• . Generalmente se completa en una cita dental
• . Reemplace los dientes perdidos al
• Implantes vs Mini Implantes
• Visite Q7z Dental para obtener una consulta complementaria y conocer cuál es la mejor opción para usted. Dependiendo de varias condiciones, incluida de la mandíbula, se le puede recomenda un tratamiento basado en implantes o mini-implantes.
• El tratamiento con implantes o mini-implantes puede no ser adecuado para todos los pacientes. Para que los implantes tengan éxito, debe tener encías sanas y huesos adecuados para apoyar los implantes. También debe estar dispuesto a comprometerse con el mantenimiento adecuado de sus implantes o dentaduras postizas. Visite a su dentista en Q7z Dental para obtener más información.
Should not have
• blank spaces without purpose

```html
<!DOCTYPE html>
<html lang="en">
<head>
<meta charset="utf-8">
<title>Q7z Dental – Implant Brochure Outer Panels</title>
<link rel="stylesheet" href="https://fonts.googleapis.com/css2?family=Montserrat:wght@400;600;700&display=swap">
<style>
  :root{
    --page:#e9ebee;
    --blue-deep:#1b5a98;
    --blue-mid:#2378b8;
    --blue-glow:#2fa3dc;
    --green:#6cbf3f;
    --green-light:#b9dc3c;
    --lime:#d8e84a;
    --white:#ffffff;
    --panel-light:#f1f2f3;
    --photo-warm:#eadcc6;
    --photo-cool:#dfe4ea;
    --photo-skin:#e8cdb4;
  }
  *{box-sizing:border-box;margin:0;padding:0}
  html,body{width:1200px;height:800px;overflow:hidden;background:var(--page);font-family:"Montserrat",sans-serif}
  .brochure{position:absolute;left:220px;top:40px;width:760px;height:720px;display:flex;box-shadow:0 10px 30px rgba(0,0,0,.18)}
  .panel{position:relative;width:380px;height:720px;overflow:hidden}

  /* mailing panel */
  .mailer{background:radial-gradient(circle at 45% 40%,var(--blue-glow) 0%,var(--blue-mid) 40%,var(--blue-deep) 85%);color:var(--white)}
  .indicia{position:absolute;top:22px;right:22px;width:90px;height:90px;background:var(--white);color:var(--blue-deep);display:flex;flex-direction:column;align-items:center;justify-content:center;text-align:center;font-size:7.5px;line-height:1.45;font-weight:600;text-transform:uppercase;border:1px solid var(--blue-deep);outline:3px solid var(--white)}
  .indicia strong{font-size:11px;font-weight:700;letter-spacing:.5px;margin:2px 0}
  .address-lines{position:absolute;left:60px;top:240px;width:270px}
  .address-lines span{display:block;height:1px;background:rgba(255,255,255,.7);margin-bottom:34px}
  .call-box{position:absolute;left:42px;top:372px;width:300px;border:1.5px solid var(--lime);padding:22px 12px 12px;text-align:center;font-size:12.5px;line-height:1.55;color:var(--white)}
  .call-tag{position:absolute;top:-13px;left:50%;transform:translateX(-50%);background:var(--lime);color:var(--white);font-weight:700;font-size:15px;letter-spacing:.5px;padding:2px 12px;white-space:nowrap}
  .web{position:absolute;left:70px;top:480px;font-size:13px;color:var(--lime);display:flex;align-items:center;gap:7px}
  .web b{font-weight:700}
  .mailer-wave{position:absolute;left:0;top:510px;width:380px;height:210px}
  .locations{position:absolute;left:58px;top:628px;color:var(--lime);font-size:13px;line-height:1.35}
  .location{display:flex;align-items:flex-start;gap:10px;margin-bottom:12px}
  .location svg{flex:none;margin-top:2px}

  /* cover panel */
  .cover{background:var(--panel-light)}
  .cover-art{position:absolute;inset:0}
  .brand{position:absolute;left:246px;top:446px;width:126px}
  .brand-name{display:flex;align-items:center;gap:6px;color:var(--blue-mid);font-weight:700;font-size:17px;white-space:nowrap}
  .brand-dot{width:14px;height:14px;border-radius:50%;background:var(--blue-mid);flex:none}
  .brand-sub{font-size:7.5px;letter-spacing:1px;color:var(--blue-mid);text-transform:uppercase;margin:2px 0 0 20px;white-space:nowrap}
  .site-pill{margin-top:8px;background:var(--blue-mid);color:var(--lime);font-size:10px;padding:4px 8px;border-radius:3px;display:inline-flex;align-items:center;gap:5px;white-space:nowrap}
  .tagline{position:absolute;right:16px;top:628px;text-align:right;color:var(--white)}
  .tagline h2{font-size:17px;font-weight:700;line-height:1.2}
  .tagline p{font-size:11px;color:var(--lime);font-weight:600;margin-top:3px}
</style>
</head>
<body>
<main class="brochure">

  <section class="panel mailer">
    <div class="indicia" aria-label="Postal retail indicia">
      <span>Prsrt Std</span>
      <strong>ECRWSS</strong>
      <span>U.S. Postage Paid</span>
      <span>WRBP Retail®</span>
    </div>

    <div class="address-lines" aria-hidden="true"><span></span><span></span><span></span></div>

    <div class="call-box">
      <span class="call-tag">CALL TOLL FREE:</span>
      1-877-Q7Z-CARE [1-877-797-2273]<br>
      Press 1 for Fenwick<br>
      Press 2 for Eastgate - Brindle Park
    </div>

    <div class="web">
      <svg width="12" height="12" viewBox="0 0 12 12" aria-hidden="true"><circle cx="6" cy="6" r="5" fill="none" stroke="currentColor" stroke-width="1.3"/><path d="M1 6h10M6 1c-2.5 3-2.5 7 0 10M6 1c2.5 3 2.5 7 0 10" fill="none" stroke="currentColor" stroke-width="1"/></svg>
      <span>www.<b>q7zdental</b>.com</span>
    </div>

    <svg class="mailer-wave" viewBox="0 0 380 210" aria-hidden="true">
      <path d="M0 88 Q170 12 380 4 L380 30 Q180 38 0 112 Z" fill="var(--lime)"/>
      <path d="M0 100 Q175 26 380 20 L380 40 Q185 48 0 122 Z" fill="var(--white)"/>
      <path d="M0 118 Q185 46 380 38 L380 210 L0 210 Z" fill="var(--blue-mid)"/>
    </svg>

    <div class="locations">
      <div class="location">
        <svg width="14" height="20" viewBox="0 0 14 20" aria-hidden="true"><path d="M7 0a7 7 0 0 0-7 7c0 5 7 13 7 13s7-8 7-13a7 7 0 0 0-7-7z" fill="var(--lime)"/><circle cx="7" cy="7" r="2.6" fill="var(--blue-mid)"/></svg>
        <span>2817 Larkmoor Ave,<br>Fenwick, MD 20799</span>
      </div>
      <div class="location">
        <svg width="14" height="20" viewBox="0 0 14 20" aria-hidden="true"><path d="M7 0a7 7 0 0 0-7 7c0 5 7 13 7 13s7-8 7-13a7 7 0 0 0-7-7z" fill="var(--lime)"/><circle cx="7" cy="7" r="2.6" fill="var(--blue-mid)"/></svg>
        <span>7431 Ashgrove Pkwy,<br>Brindle Park, MD 20977</span>
      </div>
    </div>
  </section>

  <section class="panel cover">
    <svg class="cover-art" viewBox="0 0 380 720" width="380" height="720">
      <defs>
        <linearGradient id="cornerGreen" x1="0" y1="0" x2="1" y2="1">
          <stop offset="0" stop-color="var(--green)"/>
          <stop offset="1" stop-color="var(--green-light)"/>
        </linearGradient>
        <linearGradient id="photoTone" x1="0" y1="0" x2="1" y2="1">
          <stop offset="0" stop-color="var(--photo-cool)"/>
          <stop offset=".55" stop-color="var(--photo-warm)"/>
          <stop offset="1" stop-color="var(--photo-skin)"/>
        </linearGradient>
      </defs>
      <path d="M190 0 L380 0 L380 260 Q330 60 190 0 Z" fill="url(#cornerGreen)"/>
      <path d="M0 610 Q160 570 380 528 L380 720 L0 720 Z" fill="var(--blue-mid)"/>
      <path d="M0 602 Q160 562 380 520" fill="none" stroke="var(--green)" stroke-width="4"/>

      <g role="img" aria-label="Photo: senior couple at the breakfast table, she smiling and holding a red apple">
        <path d="M190 40 Q368 40 360 250 Q352 420 190 425 Q28 420 22 255 Q18 60 190 40 Z" fill="url(#photoTone)" stroke="var(--green)" stroke-width="5"/>
      </g>
      <g role="img" aria-label="Photo: group of cheerful seniors giving thumbs up">
        <circle cx="95" cy="470" r="52" fill="var(--photo-warm)" stroke="var(--green)" stroke-width="4"/>
      </g>
      <g role="img" aria-label="Photo: smiling senior couple cheek to cheek">
        <circle cx="185" cy="540" r="66" fill="var(--photo-skin)" stroke="var(--green)" stroke-width="4"/>
      </g>
    </svg>

    <div class="brand">
      <div class="brand-name"><span class="brand-dot"></span>Q7z Dental</div>
      <div class="brand-sub">Family Dentistry</div>
      <div class="site-pill">
        <svg width="10" height="10" viewBox="0 0 12 12" aria-hidden="true"><circle cx="6" cy="6" r="5" fill="none" stroke="currentColor" stroke-width="1.3"/><path d="M1 6h10M6 1c-2.5 3-2.5 7 0 10M6 1c2.5 3 2.5 7 0 10" fill="none" stroke="currentColor" stroke-width="1"/></svg>
        <span>www.q7zdental.com</span>
      </div>
    </div>

    <div class="tagline">
      <h2>Implants &amp;<br>Mini Implants</h2>
      <p>Your Implant Destination.</p>
    </div>
  </section>

</main>
</body>
</html>
```